Clearwater Renewal Pathway Institute Second Chance Recovery Services

Logo needs to incorporate that we are here to help support positive healthy lifestyle change and help with restoration of drivers license after getting caught driving under the influence of alcohol or other drugs. While enrolled in our 3-,6-, or 9-mo program we help clients explore their relationship with alcohol or other drugs and and seek help and support so that can overcome barriers that support a healthy life style supporting client decisions to change risky behavior like driving under the influence of alcohol or drugs.

Target Market(s)

DWI / DUI Clients

Contact Information for Business Card

Logo that signifies supportive services for positive change

Requirements
Must have
• Its more of a Alcohol and drug program / Interventions for self assessment / evaluation of relationship with alcohol or drug and or risky behavior s
Should not have
• Cars on indication of cars sales

```html
<!DOCTYPE html>
<html lang="en">
<head>
<meta charset="utf-8">
<title>Clearwater Renewal Pathway Institute – Stationery</title>
<link rel="stylesheet" href="https://fonts.googleapis.com/css2?family=Cinzel:wght@500;700&family=Open+Sans:wght@400&display=swap">
<style>
  :root {
    --paper: #ffffff;
    --brand-red: #c4232f;
    --deep-red: #8e1b1f;
    --band-blue: #1f7fc1;
    --band-blue-dark: #176aa6;
    --band-navy: #35449a;
    --band-navy-dark: #2b3886;
    --icon-orange: #e07a12;
    --icon-red: #c0202b;
    --icon-navy: #1f2f6e;
  }
  html, body {
    margin: 0;
    padding: 0;
    width: 1200px;
    height: 1200px;
    overflow: hidden;
    background: var(--paper);
  }
  .canvas {
    position: relative;
    width: 1200px;
    height: 1200px;
    background: var(--paper);
  }
  .brand {
    position: absolute;
    display: flex;
    align-items: flex-start;
    gap: 12px;
    font-family: "Cinzel", Georgia, serif;
    font-weight: 700;
    color: var(--brand-red);
  }
  .brand-square {
    width: 18px;
    height: 18px;
    margin-top: 8px;
    background: var(--brand-red);
    flex: none;
  }
  .brand-name {
    margin: 0;
    font-size: 30px;
    line-height: 1.1;
    letter-spacing: 0.5px;
  }
  .brand-tagline {
    margin: 8px 0 0;
    font-size: 12px;
    letter-spacing: 4px;
    text-transform: uppercase;
  }
  .brand--front { left: 470px; top: 250px; }
  .brand--back { left: 215px; top: 580px; }

  .band {
    position: absolute;
    overflow: visible;
  }
  .band--front { left: 332px; top: 392px; }
  .band--back { left: 174px; top: 795px; }

  .contact-name {
    position: absolute;
    left: 713px;
    top: 518px;
    margin: 0;
    font-family: "Cinzel", Georgia, serif;
    font-weight: 500;
    font-size: 19px;
    color: var(--deep-red);
  }
  .contact-list {
    position: absolute;
    left: 710px;
    top: 612px;
    margin: 0;
    padding: 0;
    list-style: none;
  }
  .contact-item {
    display: flex;
    align-items: center;
    gap: 18px;
    height: 34px;
    margin-bottom: 17px;
  }
  .contact-icon { width: 34px; height: 34px; flex: none; }
  .contact-phone { font-family: "Cinzel", Georgia, serif; font-size: 17px; color: var(--deep-red); font-weight: 700; }
  .contact-email { font-family: "Open Sans", Arial, sans-serif; font-size: 15px; color: var(--deep-red); }
  .contact-web { font-family: "Cinzel", Georgia, serif; font-size: 11.5px; color: #333; }
</style>
</head>
<body>
<main class="canvas">
  <svg width="0" height="0" style="position:absolute">
    <defs>
      <filter id="band-shadow" x="-5%" y="-30%" width="110%" height="160%">
        <feDropShadow dx="0" dy="2" stdDeviation="3" flood-color="#000" flood-opacity="0.35"/>
      </filter>
      <linearGradient id="blue-fill" x1="0" y1="0" x2="0" y2="1">
        <stop offset="0" stop-color="var(--band-blue-dark)"/>
        <stop offset="1" stop-color="var(--band-blue)"/>
      </linearGradient>
      <linearGradient id="navy-fill" x1="0" y1="0" x2="0" y2="1">
        <stop offset="0" stop-color="var(--band-navy-dark)"/>
        <stop offset="1" stop-color="var(--band-navy)"/>
      </linearGradient>
    </defs>
  </svg>

  <!-- Front card -->
  <div class="brand brand--front">
    <span class="brand-square"></span>
    <div>
      <p class="brand-name">Clearwater Renewal<br>Pathway Institute</p>
      <p class="brand-tagline">Second Chance Recovery Services</p>
    </div>
  </div>

  <svg class="band band--front" width="548" height="84" viewBox="0 0 548 84">
    <path d="M6 8 C 150 10, 260 40, 400 34 C 470 30, 520 22, 542 22 L 542 76 L 6 76 Z"
          fill="url(#blue-fill)" stroke="#fff" stroke-width="3" filter="url(#band-shadow)"/>
  </svg>

  <!-- Back card -->
  <div class="brand brand--back">
    <span class="brand-square"></span>
    <div>
      <p class="brand-name">Clearwater Renewal<br>Pathway Institute</p>
      <p class="brand-tagline">Second Chance Recovery Services</p>
    </div>
  </div>

  <p class="contact-name">NAME............</p>
  <ul class="contact-list">
    <li class="contact-item">
      <svg class="contact-icon" viewBox="0 0 34 34" aria-hidden="true">
        <circle cx="17" cy="17" r="16" fill="var(--icon-orange)"/>
        <path d="M12 9 l3 0 l1.5 4.5 l-2 1.5 c1 2.5 2.5 4 5 5 l1.5 -2 l4.5 1.5 l0 3 c0 1 -1 2 -2 2 c-7 -0.5 -12.5 -6 -13 -13 c0 -1 1 -2 2 -2.5 z" fill="#fff"/>
      </svg>
      <span class="contact-phone">+.............</span>
    </li>
    <li class="contact-item">
      <svg class="contact-icon" viewBox="0 0 34 34" aria-hidden="true">
        <circle cx="17" cy="17" r="16" fill="var(--icon-red)"/>
        <rect x="9" y="11" width="16" height="12" fill="none" stroke="#fff" stroke-width="1.6"/>
        <path d="M9 11 L17 18 L25 11" fill="none" stroke="#fff" stroke-width="1.6"/>
      </svg>
      <span class="contact-email">hello@renewalpathway.org</span>
    </li>
    <li class="contact-item">
      <svg class="contact-icon" viewBox="0 0 34 34" aria-hidden="true">
        <circle cx="17" cy="17" r="16" fill="var(--icon-navy)"/>
        <g fill="none" stroke="#fff" stroke-width="1.3">
          <circle cx="17" cy="17" r="8"/>
          <ellipse cx="17" cy="17" rx="3.5" ry="8"/>
          <line x1="9" y1="17" x2="25" y2="17"/>
          <line x1="10.5" y1="13" x2="23.5" y2="13"/>
          <line x1="10.5" y1="21" x2="23.5" y2="21"/>
        </g>
      </svg>
      <span class="contact-web">WWW.CLEARWATERRENEWAL.ORG</span>
    </li>
  </ul>

  <svg class="band band--back" width="876" height="122" viewBox="0 0 876 122">
    <path d="M6 6 C 150 30, 300 52, 480 52 C 640 52, 780 40, 866 38 L 866 112 L 6 114 Z"
          fill="url(#navy-fill)" stroke="#fff" stroke-width="3" filter="url(#band-shadow)"/>
  </svg>
</main>
</body>
</html>
```